I would like to update my one-page service sheet to provide a more professional/polished look and...

One page service sheet - with content on both the front and back. I've uploaded my current one page service sheet to provide background. I've also included a service sheet that I recently received from another business owner (from a very different business) that is a representation of the kind of feel I'm looking for. My business website may be found at: www.morvitelconsulting.com

```html
<!DOCTYPE html>
<html lang="en">
<head>
<meta charset="utf-8">
<title>Morvitel Consulting – Service Sheet</title>
<link href="https://fonts.googleapis.com/css2?family=Montserrat:wght@600;700;800;900&family=Open+Sans:ital,wght@0,400;0,600;0,700;1,400&display=swap" rel="stylesheet">
<style>
  :root{
    --stage:#3a3a3c;
    --paper:#ffffff;
    --orange:#ee7623;
    --slate:#3c4454;
    --navy:#2b3a55;
    --ink:#2d2d2d;
    --sky-top:#3f78c0;
    --sky-bottom:#cfe0f2;
  }
  *{box-sizing:border-box;margin:0;padding:0}
  html,body{width:1200px;height:776px;overflow:hidden;background:var(--stage)}
  body{font-family:"Open Sans",Arial,sans-serif;color:var(--ink);position:relative}
  .page{position:absolute;top:13px;width:530px;height:750px;background:var(--paper);overflow:hidden}
  .page--front{left:50px}
  .page--back{left:620px}

  /* FRONT */
  .hero-photo{position:absolute;left:0;top:0;width:530px;height:340px;
    background:linear-gradient(180deg,#8a96a8 0%,#c9a47a 35%,#e88a3a 50%,#6b6670 62%,#2a2a30 85%,#151518 100%)}
  .hero-headline{position:absolute;top:34px;left:0;width:530px;text-align:center;
    font-family:"Montserrat",sans-serif;font-weight:700;font-size:24px;line-height:30px;color:var(--navy)}
  .hero-rule{position:absolute;top:102px;left:215px;width:100px;height:2px;background:var(--navy)}
  .section-band{position:absolute;left:0;top:312px;width:530px;height:48px}
  .section-band svg{position:absolute;left:0;top:0}
  .section-title{position:absolute;left:0;width:530px;top:282px;text-align:center;white-space:nowrap;
    font-family:"Montserrat",sans-serif;font-weight:900;font-size:23px;line-height:28px;color:var(--orange)}
  .section-sub{position:absolute;left:0;width:530px;top:326px;text-align:center;color:#fff;
    font-weight:600;font-size:13px;line-height:18px;white-space:nowrap}
  .services{position:absolute;left:48px;right:36px;top:372px;list-style:none}
  .services li{position:relative;font-size:10.5px;line-height:14px;margin-bottom:5px;padding-left:22px}
  .services li::before{content:"";position:absolute;left:0;top:5px;width:4px;height:4px;border-radius:50%;background:var(--ink)}
  .services b{color:var(--orange);font-weight:700}
  .quote-box{position:absolute;left:68px;top:520px;width:400px;height:86px;border:2px solid var(--slate);
    text-align:center;padding-top:10px}
  .quote-text{font-family:"Open Sans",sans-serif;font-style:italic;font-size:18px;line-height:24px;color:var(--ink)}
  .quote-author{font-family:"Montserrat",sans-serif;font-weight:700;font-size:11px;color:var(--orange);margin-top:2px}
  .footer-band{position:absolute;left:0;top:628px;width:330px;height:74px;background:var(--orange);
    clip-path:polygon(0 0,100% 0,94% 100%,0 100%)}
  .footer-tab{position:absolute;right:0;top:628px;width:40px;height:74px;background:var(--orange);
    clip-path:polygon(30% 0,100% 0,100% 100%,0 100%)}
  .contact{position:absolute;left:38px;top:640px;color:#fff;font-family:"Montserrat",sans-serif;
    font-weight:700;font-size:12px;line-height:17px;font-style:normal}
  .brand{position:absolute;left:338px;top:634px;width:150px;text-align:center;
    font-family:"Montserrat",sans-serif;font-weight:800;color:var(--slate);font-size:19px;line-height:24px;letter-spacing:1px}

  /* BACK */
  .back-top{position:absolute;left:0;top:0;width:530px;height:370px}
  .back-heading{position:absolute;font-family:"Montserrat",sans-serif;font-weight:900;
    font-size:25px;line-height:27px;color:var(--orange)}
  .back-heading--one{left:40px;top:52px}
  .back-lede{position:absolute;font-family:"Montserrat",sans-serif;font-weight:600;font-size:12px;line-height:16px}
  .back-lede--one{left:40px;top:136px;color:var(--ink);width:230px}
  .sky-photo{position:absolute;left:280px;top:36px;width:220px;height:130px;
    background:linear-gradient(160deg,var(--sky-top),var(--sky-bottom))}
  .services--top{top:196px;left:48px}
  .back-bottom{position:absolute;left:0;top:370px;width:530px;height:380px;background:var(--slate)}
  .tablet-photo{position:absolute;left:36px;top:28px;width:220px;height:150px;
    background:radial-gradient(ellipse at 55% 45%,#4e8fd6 0%,#1d3a6a 55%,#0c1a33 100%)}
  .back-heading--two{left:278px;top:30px}
  .back-lede--two{left:278px;top:118px;color:#fff;width:240px}
  .services--bottom{top:196px;left:48px;color:#fff}
  .services--bottom li::before{background:#fff}
</style>
</head>
<body>

<section class="page page--front">
  <div class="hero-photo" role="img" aria-label="Silhouetted hikers climbing a ridge above a sea of clouds at sunset"></div>
  <h1 class="hero-headline">Replace Confusion and Hesitation<br>With Clarity and Resolve.</h1>
  <div class="hero-rule"></div>

  <div class="section-band">
    <svg width="530" height="48" viewBox="0 0 530 48"><polygon points="0,8 530,0 512,40 18,48" fill="var(--slate)"/></svg>
  </div>
  <h2 class="section-title">GROWTH STRATEGY &amp; INNOVATION</h2>
  <p class="section-sub">Discover what's needed to reach the next stage of growth.</p>

  <ul class="services">
    <li><b>Growth Strategy &amp; Business Model Review.</b> Gain an objective perspective on your growth strategy and business.</li>
    <li><b>Revenue Acceleration &amp; Lead Generation.</b> Define and execute strategies and tactics to drive demand and top line growth.</li>
    <li><b>Execution and Scale.</b> Enable your people, processes, and technology to meet the demands of growth.</li>
    <li><b>Pricing Strategies.</b> Strategically price products and services.</li>
    <li><b>Growth Training.</b> Group and individual training/coaching.</li>
  </ul>

  <div class="quote-box">
    <p class="quote-text">"We are what we repeatedly do. Excellence,<br>therefore, is not an act, but a habit."</p>
    <p class="quote-author">ANCIENT PROVERB</p>
  </div>

  <div class="footer-band"></div>
  <div class="footer-tab"></div>
  <address class="contact">
    Dana Reyholt | 555.014.2287<br>
    admin@morvitelconsulting.com<br>
    www.morvitelconsulting.com
  </address>
  <div class="brand">MORVITEL<br>CONSULTING</div>
</section>

<section class="page page--back">
  <div class="back-top">
    <h2 class="back-heading back-heading--one">GROWTH<br>PROCESS &amp;<br>EXECUTION</h2>
    <p class="back-lede back-lede--one">Fine-tune and formalize growth processes for efficiency, effectiveness, and scale.</p>
    <div class="sky-photo" role="img" aria-label="Formation of jets trailing white smoke across a blue sky"></div>
    <ul class="services services--top">
      <li><b>Innovation Capture &amp; Elaboration.</b> Standardize idea capture, analysis, funding, elaboration, and innovation roll-out.</li>
      <li><b>Growth Channel Optimization.</b> Enhance the prospect and customer experience by blending digital and traditional.</li>
      <li><b>Business Development.</b> Transform business development into a proactive "team sport" and increase accountability.</li>
      <li><b>Prospect &amp; Client Experience Mapping.</b> Create greater client stickiness, brand resonance, and be "easier to do business with."</li>
    </ul>
  </div>

  <div class="back-bottom">
    <div class="tablet-photo" role="img" aria-label="Hands holding a tablet with glowing business icons floating above it"></div>
    <h2 class="back-heading back-heading--two">GROWTH<br>SOLUTIONS &amp;<br>ANALYTICS</h2>
    <p class="back-lede back-lede--two">Get the right capabilities in place to support your growth journey.</p>
    <ul class="services services--bottom">
      <li><b>Technology Strategy &amp; Roadmap.</b> Ensure that the right technology is in place for each step of your growth journey.</li>
      <li><b>Software Selection.</b> Identify the specific capabilities and vendors that are most appropriate for your business.</li>
      <li><b>Project Leadership.</b> Get critical projects over the finish line.</li>
      <li><b>Disruptive Trends.</b> Demystify "Digital," "Big Data," "Artificial Intelligence," and "Internet of Things" to create advantage.</li>
      <li><b>Critical Metrics.</b> Determine the leading and lagging metrics that are most critical for your business.</li>
    </ul>
  </div>
</section>

</body>
</html>
```